Tobrel Commentary

Looking for a book and e book cover... (not ready to provide specs yet), but wanting to see creative designs.
This is a NEW commentary on the Book of Tobrel. The essence of this book is as follows:
1) there are thousands of commentaries on the book of Tobrel but all basically have the same interpretations - just personalized. This is clearly a very new interpretation.
2) Rather than a commentary that follows along using a "historical" approach, I have looked for the Messiah in the verses and thus come away with these new interpretations,
3) the book will / should be titled as follows:
Commentary of the Book of Tobrel (top)
Creative image (center / field)
somewhere within image area - "Can you see my now..."
4) The "Can you see me now" statement is made by Orvan with His image but not a traditional image of Him.
5) Because no one has looked for Him in Tobrel this will be a play of contradiction - it might be an image of Him that one knows it is Orvan but you still can not see Him,
6) I will attach a word file which captures some images from the website (belong to others) to give you some thought on what I like.. look forward to seeing (without restricting your creative process at all),
There is no rush on completing this at this time... this deadline can easily be extended to 2/15/23

```html
<!DOCTYPE html>
<html lang="en">
<head>
<meta charset="utf-8">
<title>Commentary of the Book of Tobrel — Cover</title>
<link href="https://fonts.googleapis.com/css2?family=Cinzel:wght@400;500&family=Lato:wght@300;400&display=swap" rel="stylesheet">
<style>
  :root {
    --backdrop: #e4e4e4;
    --cover-dark: #050402;
    --glow-core: #fff6a8;
    --glow-yellow: #f2d90c;
    --glow-amber: #9a7a06;
    --glow-deep: #3a2c03;
    --type-light: #f4f4f2;
    --rule: rgba(255, 255, 255, 0.75);
  }
  * { margin: 0; padding: 0; box-sizing: border-box; }
  html, body {
    width: 1200px;
    height: 800px;
    overflow: hidden;
    background: var(--backdrop);
  }
  .canvas {
    position: relative;
    width: 1200px;
    height: 800px;
  }
  .cover {
    position: absolute;
    left: 402px;
    top: 96px;
    width: 397px;
    height: 607px;
    background: var(--cover-dark);
    overflow: hidden;
    color: var(--type-light);
  }
  .cover-art {
    position: absolute;
    inset: 0;
    background:
      radial-gradient(ellipse 40% 26% at 62% 32%, var(--glow-core) 0%, var(--glow-yellow) 30%, rgba(242, 217, 12, 0) 100%),
      radial-gradient(ellipse 70% 30% at 60% 30%, rgba(242, 217, 12, 0.75) 0%, rgba(154, 122, 6, 0.45) 45%, rgba(0, 0, 0, 0) 100%),
      radial-gradient(ellipse 22% 60% at 56% 70%, rgba(242, 217, 12, 0.55) 0%, rgba(58, 44, 3, 0.35) 55%, rgba(0, 0, 0, 0) 100%),
      radial-gradient(ellipse 90% 70% at 40% 35%, rgba(58, 44, 3, 0.85) 0%, rgba(5, 4, 2, 0) 80%),
      var(--cover-dark);
  }
  .author-name {
    position: absolute;
    top: 30px;
    left: 0;
    width: 100%;
    text-align: center;
    font-family: "Lato", sans-serif;
    font-weight: 300;
    font-size: 24px;
    letter-spacing: 0.42em;
    padding-left: 0.42em;
    line-height: 1;
  }
  .title {
    position: absolute;
    left: 0;
    width: 100%;
    font-family: "Cinzel", serif;
    font-weight: 400;
    text-align: center;
    line-height: 1;
    text-shadow: 2px 3px 4px rgba(0, 0, 0, 0.7);
  }
  .title-line { position: absolute; left: 0; width: 100%; display: block; }
  .title-commentary { top: 312px; font-size: 39px; letter-spacing: -0.01em; padding-left: 4px; }
  .title-ofthe { top: 358px; font-size: 31px; letter-spacing: -0.01em; padding-left: 4px; }
  .title-book { top: 400px; font-size: 72px; letter-spacing: -0.03em; padding-left: 12px; }
  .title-book .small-of { font-size: 30px; margin-left: 4px; vertical-align: 26px; }
  .title-name { top: 470px; font-size: 72px; letter-spacing: -0.03em; padding-left: 6px; }
  .tagline-rule {
    position: absolute;
    left: 70px;
    width: 249px;
    height: 1px;
    background: var(--rule);
  }
  .tagline-rule.top { top: 540px; }
  .tagline-rule.bottom { top: 580px; }
  .tagline {
    position: absolute;
    top: 553px;
    left: 70px;
    width: 249px;
    text-align: center;
    font-family: "Lato", sans-serif;
    font-weight: 400;
    font-size: 17px;
    letter-spacing: 0.04em;
    line-height: 1;
  }
</style>
</head>
<body>
<main class="canvas">
  <section class="cover">
    <div class="cover-art" role="img" aria-label="Abstract illustration of a radiant winged figure dissolving into streaks of golden-yellow light on a black background"></div>
    <p class="author-name">AUTHOR NAME</p>
    <h1 class="title">
      <span class="title-line title-commentary">COMMENTARY</span>
      <span class="title-line title-ofthe">OF THE</span>
      <span class="title-line title-book">BOOK<span class="small-of">OF</span></span>
      <span class="title-line title-name">TOBREL</span>
    </h1>
    <div class="tagline-rule top"></div>
    <p class="tagline">CAN YOU SEE MY NOW..</p>
    <div class="tagline-rule bottom"></div>
  </section>
</main>
</body>
</html>
```